Medical Company in need of a Modern Flyer design for new Wound Care clinic.

Tri-Fold modern flyer design for our Woundcare company. Logo and description of services can be found on our website; https://www.birchline-woundcare.com/

```html
<!DOCTYPE html>
<html lang="en">
<head>
<meta charset="utf-8">
<title>Birchline Woundcare – Tri-Fold Brochure</title>
<link href="https://fonts.googleapis.com/css2?family=Montserrat:wght@300;400;500;700&display=swap" rel="stylesheet">
<style>
:root{
  --bg:#c4c4c4;
  --gold-light:#f7c977;
  --gold:#e0ae5b;
  --gold-deep:#c8963f;
  --charcoal:#3f3e40;
  --slate:#6b6a6d;
  --ink:#222;
  --white:#fff;
  --text-soft:#f2f2f2;
}
*{box-sizing:border-box;margin:0;padding:0}
html,body{width:900px;height:1200px;overflow:hidden}
body{background:var(--bg);font-family:"Montserrat",sans-serif;color:var(--ink);position:relative}
.spread{position:absolute;left:120px;width:635px;height:489px;box-shadow:0 14px 22px rgba(0,0,0,.35);overflow:hidden;background:var(--white)}
.spread--outside{top:60px}
.spread--inside{top:627px}
.edge{position:absolute;left:0;width:100%;height:4px;background:linear-gradient(90deg,var(--gold) 0 33.4%,var(--gold-deep) 33.4% 66.6%,var(--charcoal) 66.6%)}
.edge--top{top:0}.edge--bottom{bottom:0}
.panel{position:absolute;top:0;height:100%;width:212px}
.p1{left:0}.p2{left:212px;width:211px}.p3{left:423px}
.gold-fill{background:linear-gradient(135deg,var(--gold-deep),var(--gold-light) 70%,var(--gold))}
.dark-fill{background:linear-gradient(135deg,var(--charcoal) 30%,var(--slate))}
.abs{position:absolute}
.tab{position:absolute;padding:0 7px;display:flex;align-items:center;font-size:12px;font-weight:400}
.tab--dark{background:linear-gradient(180deg,var(--charcoal),var(--slate));color:var(--white)}
.tab--gold{background:linear-gradient(180deg,var(--gold),var(--gold-light));color:var(--ink)}
ul.list{list-style:none;font-size:7.6px;line-height:9.4px;font-weight:400}
ul.list li{position:relative;padding-left:9px;margin-bottom:6px}
ul.list li::before{content:"";position:absolute;left:0;top:3px;width:3px;height:3px;background:currentColor}
ul.list--gold li::before{background:var(--gold)}
ul.tight li{margin-bottom:2.6px}
.feature{position:absolute;left:22px;width:175px;color:var(--text-soft)}
.feature h3{display:flex;gap:6px;font-size:9.5px;font-weight:400;line-height:11px;color:var(--white);margin-bottom:8px}
.feature .icon{width:18px;height:18px;flex:none;background:var(--gold);border:1px solid var(--gold-light)}
.feature p,.body{font-size:7.5px;line-height:9.4px;font-weight:300}
.body{text-align:justify}
.photo{position:absolute}
.brand{font-size:14px;letter-spacing:4px;font-weight:400;color:var(--charcoal);text-align:center}
.phone-bar{display:flex;height:22px;width:162px}
.phone-bar .ico{width:22px;background:var(--gold);display:flex;align-items:center;justify-content:center}
.phone-bar .num{flex:1;background:var(--charcoal);color:var(--white);font-weight:700;font-size:16px;display:flex;align-items:center;justify-content:center;letter-spacing:.5px}
.web{font-size:11.5px;font-weight:400}
.web b{color:var(--gold-deep);font-weight:500}
.small-ico{display:inline-block;width:11px;height:11px;background:var(--gold);vertical-align:-2px;margin-right:5px}
h2.head{font-size:12.5px;font-weight:500;line-height:14px;color:var(--charcoal)}
</style>
</head>
<body>

<!-- Outside spread -->
<section class="spread spread--outside">
  <div class="panel p1">
    <div class="abs gold-fill" style="left:0;top:0;width:212px;height:156px"></div>
    <div class="abs dark-fill" style="left:0;top:156px;width:212px;height:333px"></div>
    <div class="tab tab--dark" style="left:20px;top:0;height:46px;width:85px">Our Services</div>
    <ul class="list" style="position:absolute;left:20px;top:55px;width:180px;color:var(--charcoal)">
      <li>Hyperbaric Oxygen Therapy (HBO):<br>A Cornerstone of Advanced Wound Care</li>
      <li>Debridement</li>
      <li>Advanced Wound Dressings</li>
      <li>Bio-engineered Skin Substitutes</li>
      <li>Compression Therapy and Edema Management</li>
    </ul>
    <div class="feature" style="top:177px">
      <h3><span class="icon"></span><span>Accepted<br>Health Plans</span></h3>
      <p>We accept most major insurance plans to make your care as accessible and affordable as possible!</p>
    </div>
    <div class="feature" style="top:254px">
      <h3><span class="icon"></span><span>Expert<br>Medical Team</span></h3>
      <p>Comprised of highly trained physicians, nurses, and specialists, our team brings years of experience in treating a wide range of complex wounds. With a commitment to innovative treatments and personalized care plans, we work closely with each patient to ensure optimal healing and recovery. Trust our team to provide the expert care you need for lasting results.</p>
    </div>
    <div class="feature" style="top:388px">
      <h3><span class="icon"></span><span>Trusted<br>Healthcare Provider</span></h3>
      <p>We specialize in advanced treatment modalities, using a multi-faceted approach to heal your patient's wound.</p>
    </div>
  </div>

  <div class="panel p2">
    <div class="abs" style="left:24px;top:20px;font-size:11px;font-weight:500">Book Your Appointment Online</div>
    <div class="abs phone-bar" style="left:24px;top:35px">
      <div class="ico"><svg width="12" height="12" viewBox="0 0 24 24"><path d="M6.6 10.8a15 15 0 0 0 6.6 6.6l2.2-2.2a1 1 0 0 1 1-.25 11.4 11.4 0 0 0 3.6.6 1 1 0 0 1 1 1V20a1 1 0 0 1-1 1A17 17 0 0 1 3 4a1 1 0 0 1 1-1h3.5a1 1 0 0 1 1 1c0 1.25.2 2.45.6 3.6a1 1 0 0 1-.25 1z" fill="#222"/></svg></div>
      <div class="num">555-014-2290</div>
    </div>
    <div class="abs web" style="left:24px;top:60px">www.<b>birchline-woundcare</b>.com</div>
    <div class="abs" style="left:24px;top:82px;font-size:8.6px"><span class="small-ico"></span>4120 Meadow Ridge Rd. Bldg. C, suite 210</div>
    <div class="abs" style="left:66px;top:99px;font-size:8.6px"><span class="small-ico"></span>555-014-2291</div>

    <div class="abs" style="left:20px;top:370px;width:171px;height:64px;border:1px solid #555;border-radius:4px"></div>
    <div class="abs" style="left:55px;top:364px;padding:0 4px;background:var(--white);font-size:8.4px">Accepted Health Plans</div>
    <div class="abs" style="left:36px;top:385px;width:38px;height:11px;background:#2d3a6b;border-radius:2px"></div>
    <div class="abs" style="left:92px;top:382px;width:28px;height:16px;background:#2b5ea7;border-radius:50%"></div>
    <div class="abs" style="left:136px;top:385px;width:38px;height:11px;background:#3ba57a;border-radius:2px"></div>
    <div class="abs" style="left:62px;top:409px;width:34px;height:14px;background:#3a7a3a;border-radius:2px"></div>
    <div class="abs" style="left:112px;top:412px;width:36px;height:8px;background:#2a3d8f;border-radius:2px"></div>
    <p class="abs" style="left:18px;top:441px;width:175px;font-size:5.2px;line-height:6.6px;text-align:center;color:#333">At our clinic, we accept a variety of health insurance plans to ensure that you receive the care you need. If your current plan is not listed, please get in touch with us so we can explore alternative options that best suit your needs.</p>
  </div>

  <div class="photo" role="img" aria-label="Bright modern clinic waiting lounge with large windows, blue chairs and plants" style="left:212px;top:121px;width:423px;height:235px;background:linear-gradient(180deg,#e8ecef 0%,#d6dade 45%,#c4b49c 80%,#b9a78d 100%)"></div>

  <div class="panel p3">
    <div class="abs" style="left:0;top:0;width:212px;height:121px;background:linear-gradient(90deg,#f2f2f2,var(--white))"></div>
    <div class="abs" style="left:98px;top:38px;width:16px;height:16px;background:var(--gold)"></div>
    <div class="abs brand" style="left:0;top:74px;width:212px">BIRCHLINE WOUNDCARE</div>
    <div class="abs gold-fill" style="left:0;top:356px;width:212px;height:133px"></div>
    <div class="abs" style="left:0;top:369px;width:212px;text-align:center;font-size:19px;line-height:22px;color:var(--ink)">Caring for Your<br>Well-being</div>
    <p class="abs" style="left:22px;top:414px;width:168px;text-align:center;font-size:7.6px;line-height:9.4px;color:#333">At Birchline Woundcare, we specialize in managing outpatient wound care facilities throughout the Dallas/Fort Worth area.</p>
    <div class="abs web" style="left:0;top:455px;width:212px;text-align:center;color:var(--ink)">www.<b style="color:var(--ink)">birchline-woundcare</b>.com</div>
  </div>
  <div class="edge edge--top"></div>
  <div class="edge edge--bottom"></div>
</section>

<!-- Inside spread -->
<section class="spread spread--inside">
  <div class="panel p1 dark-fill">
    <div class="photo" role="img" aria-label="Hyperbaric oxygen chamber with a padded treatment bed" style="left:0;top:0;width:212px;height:162px;background:linear-gradient(135deg,#f3f2ec,#d8d6cc 60%,#b6b3a6)"></div>
    <div class="tab tab--gold" style="left:18px;top:162px;height:46px;width:94px">Wound Types</div>
    <ul class="list list--gold tight" style="position:absolute;left:18px;top:223px;width:85px;color:var(--text-soft)">
      <li>Atypical Wounds</li><li>Bone Infections</li><li>Burn Wounds</li><li>Chronic Wounds</li><li>Diabetic Ulcers</li><li>Diabetic Wounds</li><li>Infected Wounds</li>
    </ul>
    <ul class="list list--gold tight" style="position:absolute;left:100px;top:223px;width:100px;color:var(--text-soft)">
      <li>Pressure Ulcers</li><li>Venous Leg Ulcers</li><li>Venous &amp; Arterial Ulcers</li><li>Surgical Wound Complications</li><li>Non-Healing Surgical Wounds</li>
    </ul>
    <p class="abs body" style="left:18px;top:310px;width:168px;color:var(--text-soft)">At Birchline Woundcare we specialize in treating a wide range of complex and hard-to-heal wounds. Our expert team is equipped to care for atypical wounds, bone infections, burn wounds, chronic wounds, and diabetic ulcers. We also provide advanced care for non-healing surgical wounds, infected wounds, pilonidal cysts, pressure ulcers, and surgical wound complications. Additionally, we treat venous and arterial ulcers, including venous leg ulcers, using the latest techniques and personalized care plans to promote healing and prevent complications. No matter the wound type, our focus is on achieving optimal outcomes for every patient.</p>
  </div>

  <div class="panel p2 gold-fill">
    <h2 class="abs head" style="left:20px;top:16px;width:180px">Hyperbaric Oxygen Therapy:<br>A Cornerstone of Advanced<br>Wound Care</h2>
    <p class="abs body" style="left:20px;top:70px;width:176px;color:#4a3d28">Hyperbaric Oxygen Therapy (HBO) is not just a treatment; it's a pivotal part of our comprehensive approach to wound healing at Birchline Woundcare. By delivering pure oxygen in a pressurized chamber, HBO therapy significantly increases the amount of oxygen in the blood, fostering an environment that accelerates the repair and regeneration of wounded tissues.</p>
    <h2 class="abs head" style="left:20px;top:158px;width:180px">How HBO Benefits<br>Wound Healing:</h2>
    <p class="abs body" style="left:20px;top:192px;width:176px;color:#4a3d28">Enhanced Oxygen Supply: Increases the oxygen level in blood and tissues, which is crucial for healing damaged cells. Stimulation of New Blood Vessels: Encourages the formation of new blood vessels, improving blood flow to areas with impaired circulation. Enhanced White Blood Cell Action: Aids the body's immune system in fighting infection and bacteria at the wound site. Reduction of Swelling and Inflammation: Speeds up healing processes and reduces pain by decreasing swelling and inflammation. Fibroblast Activation: Promotes collagen production, which is vital for wound closure and strength.</p>
    <h2 class="abs head" style="left:21px;top:340px;width:180px">How HBO Benefits<br>Wound Healing:</h2>
    <p class="abs body" style="left:21px;top:370px;width:176px;color:#4a3d28">Chronic Wounds: Especially effective in treating non-healing wounds that have not improved with other treatments. Infections: Including bone infections (osteomyelitis) and diabetic foot ulcers. Crush Injuries and Radiation Injuries: Reduces swelling and improves oxygen supply to tissues that have been compromised. Skin Grafts and Flaps: Ensures the survival of these tissues by enhancing oxygenation and vascular growth.</p>
  </div>

  <div class="panel p3">
    <div class="photo" role="img" aria-label="Clinician wrapping a patient's knee with a bandage" style="left:0;top:260px;width:212px;height:229px;background:linear-gradient(180deg,#ffffff 0%,#e9edf2 30%,#d9dfe6 65%,#e6d2c4 100%)"></div>
    <div class="tab tab--gold" style="left:18px;top:0;height:46px;width:118px">Wound Treatment</div>
    <ul class="list list--gold tight" style="position:absolute;left:18px;top:57px;width:185px;color:var(--ink)">
      <li>Compression Therapy</li><li>Mechanical &amp; Enzymatic Debridement</li><li>Negative Pressure Wound Therapy</li><li>Post-Mohs Surgery</li><li>Tissue Infection Management / Labs</li><li>Total Contact Casting</li><li>Wound Care</li><li>Wound Debridement</li>
    </ul>
    <p class="abs body" style="left:18px;top:162px;width:178px;color:#444">At Birchline Woundcare we offer a full spectrum of advanced wound care treatments designed to promote healing and improve patient outcomes. Our treatments include compression therapy, mechanical and enzymatic debridement, and negative pressure wound therapy to help manage and accelerate wound healing. We also specialize in post-Mohs surgery care, tissue infection management with onsite labs, and total contact casting for diabetic foot ulcers. Whether you need wound debridement or comprehensive wound care, our expert team is here to provide personalized treatments for faster recovery and lasting results.</p>
  </div>
  <div class="edge edge--top" style="background:linear-gradient(90deg,var(--gold) 0 33.4%,var(--slate) 33.4% 66.6%,var(--gold) 66.6%)"></div>
  <div class="edge edge--bottom" style="background:linear-gradient(90deg,var(--gold) 0 33.4%,var(--charcoal) 33.4% 66.6%,var(--gold) 66.6%)"></div>
</section>

</body>
</html>
```